Equine Rescue
Print Materials Design
Simple
Larkhollow Equine Sanctuary
2710 County Road 48B
Alderbrook NY 12598
TrotMeadow@fenmail.net
www.larkhollowequinesanctuaryinc.org
501(c)(3) Charity

```html
<!DOCTYPE html>
<html lang="en">
<head>
<meta charset="utf-8">
<title>Larkhollow Equine Sanctuary – Stationery</title>
<link href="https://fonts.googleapis.com/css2?family=Arimo:wght@400;700&display=swap" rel="stylesheet">
<style>
  :root {
    --brand-blue: #1d5aa8;
    --paper: #ffffff;
    --canvas: #ffffff;
    --edge: #d9dce1;
    --flap-line: #8a8f96;
    --on-blue: #ffffff;
  }
  * { box-sizing: border-box; margin: 0; padding: 0; }
  html, body { width: 1200px; height: 681px; overflow: hidden; background: var(--canvas); }
  body { position: relative; font-family: "Arimo", Arial, sans-serif; }

  .sheet {
    position: absolute;
    background: var(--paper);
    border: 1px solid var(--edge);
    box-shadow: 2px 3px 6px rgba(0,0,0,0.12);
    overflow: hidden;
  }
  .brand-band {
    position: absolute; left: 0; right: 0;
    background: var(--brand-blue);
    color: var(--on-blue);
    font-weight: 400;
    display: flex; flex-direction: column; justify-content: center;
    white-space: nowrap;
  }
  .wordmark {
    position: absolute;
    display: flex; align-items: center; gap: 6px;
    color: var(--brand-blue);
    font-weight: 700;
    line-height: 1.1;
  }
  .wordmark-dot { border-radius: 50%; background: var(--brand-blue); flex: none; }

  /* envelope front */
  .envelope-front { left: 58px; top: 101px; width: 492px; height: 204px; }
  .envelope-front .wordmark { left: 16px; top: 14px; font-size: 13px; width: 150px; }
  .envelope-front .wordmark-dot { width: 14px; height: 14px; }
  .envelope-front .brand-band { top: 160px; height: 28px; padding-left: 18px; font-size: 8px; }

  /* envelope back */
  .envelope-back { left: 58px; top: 353px; width: 492px; height: 223px; }
  .envelope-back .flap { position: absolute; left: 0; top: 0; }
  .envelope-back .wordmark {
    left: 0; right: 0; top: 82px; justify-content: center;
    font-size: 10px;
  }

  /* letterhead */
  .letterhead { left: 619px; top: 65px; width: 336px; height: 564px; }
  .letterhead .wordmark { left: 16px; top: 12px; font-size: 14px; width: 160px; }
  .letterhead .wordmark-dot { width: 15px; height: 15px; }
  .letterhead .brand-band { top: 494px; height: 43px; padding-left: 18px; font-size: 7px; line-height: 1.5; }

  /* business card */
  .business-card { left: 970px; top: 168px; width: 114px; height: 96px; }
  .business-card .wordmark { left: 7px; top: 8px; font-size: 6.5px; width: 80px; gap: 4px; }
  .business-card .wordmark-dot { width: 7px; height: 7px; }
  .business-card .brand-band { top: 60px; height: 28px; padding-left: 7px; font-size: 4px; line-height: 1.4; }
</style>
</head>
<body>

<section class="sheet envelope-front" aria-label="Envelope front">
  <div class="wordmark"><span class="wordmark-dot"></span><span>Larkhollow Equine Sanctuary</span></div>
  <div class="brand-band">
    <p>2710 County Road 48B &nbsp;|&nbsp; Alderbrook NY 12598</p>
  </div>
</section>

<section class="sheet envelope-back" aria-label="Envelope back">
  <svg class="flap" width="492" height="223" viewBox="0 0 492 223" aria-hidden="true">
    <path d="M2 6 Q8 14 30 20 L236 68 Q246 70 256 68 L462 20 Q484 14 490 6"
          fill="none" stroke="var(--flap-line)" stroke-width="1.2"/>
  </svg>
  <div class="wordmark"><span>Larkhollow Equine Sanctuary</span></div>
</section>

<section class="sheet letterhead" aria-label="Letterhead">
  <div class="wordmark"><span class="wordmark-dot"></span><span>Larkhollow Equine Sanctuary</span></div>
  <div class="brand-band">
    <p>2710 County Road 48B &nbsp;|&nbsp; Alderbrook NY 12598</p>
    <p>Phone (845) 555-0148 &nbsp;|&nbsp; Fax (845) 555-0149</p>
    <p>www.larkhollowequinesanctuaryinc.org</p>
  </div>
</section>

<section class="sheet business-card" aria-label="Business card">
  <div class="wordmark"><span class="wordmark-dot"></span><span>Larkhollow Equine Sanctuary</span></div>
  <div class="brand-band">
    <p>2710 County Road 48B | Alderbrook NY 12598</p>
    <p>Phone (845) 555-0148 | Fax (845) 555-0149</p>
    <p>TrotMeadow@fenmail.net</p>
    <p>www.larkhollowequinesanctuaryinc.org</p>
  </div>
</section>

</body>
</html>
```